Wooden Floor Website

I'd like a Modern and crisp site with emphasis on the site being easy to navigate through - services that we offer, gallery of previous work, history, who we are, contact, etc
https://tmqrvx8219067-my.dokshelfbox.net/:b:/g/personal/marcus_bellhaven_co_uk/QWT7K2_pmRsNaHXdovtYBeLWCKjuP9e3F6kRMZbqUwnPzs

Coding

Coded - Design and coding required

Number of Pages Required

5+ page

Requirements
Must have
• Word Press Site

```html
<!DOCTYPE html>
<html lang="en">
<head>
<meta charset="utf-8">
<title>Bellhaven – Bespoke Wood Flooring</title>
<link rel="stylesheet" href="https://fonts.googleapis.com/css2?family=Poppins:wght@300;400;500;600;700&display=swap">
<style>
:root{
  --ink:#222;
  --muted:#555;
  --line:#9a9a9a;
  --panel:#f5f5f5;
  --card:#f3f3f3;
  --footer:#1f1f1f;
  --footer-line:#555;
  --white:#fff;
}
*{box-sizing:border-box;margin:0;padding:0}
html,body{width:1200px;height:4054px;overflow:hidden}
body{font-family:"Poppins",sans-serif;color:var(--ink);background:var(--white);position:relative}
.abs{position:absolute}
.photo{position:absolute;display:block}
.btn{position:absolute;border:1.5px solid #555;background:var(--white);font-size:13px;color:var(--ink);display:flex;align-items:center;justify-content:center}
.section-title{position:absolute;left:0;width:1200px;text-align:center;font-size:32px;font-weight:400;color:var(--ink)}
p.body{font-size:13px;line-height:19px;color:var(--muted)}

/* header */
.site-header{position:absolute;left:0;top:0;width:1200px;height:113px;background:var(--white)}
.menu-icon{position:absolute;left:80px;top:48px;width:20px}
.menu-icon span{display:block;height:2px;background:var(--ink);margin-bottom:4px}
.brand{position:absolute;left:500px;top:18px;width:200px;text-align:center}
.brand-mark{width:40px;height:40px;border:1.5px solid var(--ink);margin:0 auto 8px}
.brand-name{font-size:12px;font-weight:600;letter-spacing:1px}
.social{position:absolute;display:flex;gap:8px}
.social i{display:block;width:20px;height:20px;border-radius:50%;background:var(--ink)}

/* hero */
.hero{position:absolute;left:0;top:113px;width:1200px;height:601px;background:linear-gradient(120deg,#9db34a 0%,#6f8a2c 30%,#3d4a1c 65%,#6b5532 100%)}
.hero-box{position:absolute;left:103px;top:165px;width:329px;height:273px;border:2px solid rgba(255,255,255,.85)}
.hero-title{position:absolute;left:33px;top:38px;color:var(--white);font-weight:700;font-size:40px;line-height:54px;letter-spacing:1px;white-space:nowrap}
.hero-title .lead{font-size:36px}
.hero-btn{position:absolute;left:33px;top:214px;width:115px;height:32px;border:1.5px solid var(--white);color:var(--white);font-size:13px;display:flex;align-items:center;justify-content:center}
.hero-dots{position:absolute;left:1150px;top:270px}
.hero-dots i{display:block;width:6px;height:6px;background:var(--white);margin-bottom:8px}
.hero-arrows{position:absolute;left:1090px;top:525px}

/* services */
.services-sub{position:absolute;left:420px;top:795px;width:360px;text-align:center;font-size:13px;line-height:18px;color:var(--muted)}
.service-caption{position:absolute;top:1114px;width:243px;text-align:center;font-size:17px;letter-spacing:.5px}

/* gallery */
.gallery-overlay{position:absolute;left:22px;bottom:40px;width:200px;color:var(--white)}
.gallery-overlay h3{font-size:17px;font-weight:500;line-height:22px;margin-bottom:10px}
.gallery-overlay p{font-size:12px;line-height:16px}

/* history */
.history{position:absolute;left:0;top:1765px;width:1200px;height:606px;background:var(--panel)}
.history h2,.about h2{font-size:30px;font-weight:400}
.underline{width:40px;height:2px;background:var(--ink);margin:4px 0 20px}

/* about */
.eyebrow{font-size:12px;color:var(--muted)}

/* blog */
.blog-card{position:absolute;top:2854px;width:327px;height:371px;background:var(--card)}
.blog-meta{position:absolute;left:18px;top:215px;width:291px;display:flex;justify-content:space-between;align-items:center;font-size:12px;color:var(--ink)}
.blog-meta .stats{display:flex;align-items:center;gap:4px}
.blog-rule{position:absolute;left:0;top:240px;width:327px;height:1px;background:#ddd}
.blog-card h3{position:absolute;left:18px;top:252px;font-size:13px;font-weight:600}
.blog-card p{position:absolute;left:18px;top:276px;width:290px;font-size:12px;line-height:16px;color:var(--muted)}
.blog-link{position:absolute;left:18px;top:330px;font-size:12px;text-decoration:underline}

/* contact */
.field{position:absolute;border:1.5px solid #aaa;background:var(--white);font-size:12px;color:var(--muted);padding:10px}

/* footer */
.site-footer{position:absolute;left:0;top:3681px;width:1200px;height:373px;background:linear-gradient(180deg,#262626,#181818);color:var(--white)}
.footer-brand{position:absolute;left:80px;top:100px;width:160px;text-align:center}
.footer-brand .brand-mark{border-color:var(--white);width:60px;height:60px}
.footer-brand .brand-name{font-size:15px}
.footer-col h4{font-size:14px;font-weight:400;margin-bottom:4px}
.footer-col .rule{width:60px;height:1px;background:var(--footer-line);margin-bottom:14px}
.footer-col ul{list-style:none;font-size:13px;line-height:20px}
.footer-col li::before{content:"• "}
.contact-list{font-size:13px;line-height:26px}
.newsletter-input{width:275px;height:36px;background:#3a3a3a;color:#aaa;font-size:12px;display:flex;align-items:center;justify-content:center;margin:14px 0 8px}
.newsletter-btn{width:275px;height:38px;background:var(--white);color:var(--ink);font-size:13px;font-weight:600;display:flex;align-items:center;justify-content:center}
.footer-rule{position:absolute;left:81px;top:298px;width:1038px;height:1px;background:var(--footer-line)}
.copyright{position:absolute;left:81px;top:317px;font-size:12px}
.site-footer .social i{background:var(--white)}
</style>
</head>
<body>

<header class="site-header">
  <div class="menu-icon"><span></span><span></span><span></span></div>
  <div class="brand"><div class="brand-mark"></div><div class="brand-name">BELLHAVEN</div></div>
  <div class="social" style="left:1008px;top:46px"><i></i><i></i><i></i><i></i></div>
</header>

<section class="hero" role="img" aria-label="Misty forest path with tall trees">
  <div class="hero-box">
    <h1 class="hero-title"><span class="lead">CREATING YOUR</span><br>EXCEPTIONAL WOOD<br>FLOOR</h1>
    <div class="hero-btn">Read More</div>
  </div>
  <div class="hero-dots"><i></i><i></i><i></i></div>
  <svg class="hero-arrows" width="70" height="20" viewBox="0 0 70 20" fill="none" stroke="#fff" stroke-width="2">
    <path d="M4 10h22M4 10l6-6M4 10l6 6"/><path d="M44 10h22M66 10l-6-6M66 10l-6 6"/>
  </svg>
</section>

<h2 class="section-title" style="top:750px">Services</h2>
<p class="services-sub">BELLHAVEN offer a range of fully bespoke finished wood flooring in planks,</p>
<div class="photo" style="left:211px;top:860px;width:243px;height:232px;background:linear-gradient(160deg,#e9e6e1,#8c7e6c 60%,#6e6254)" role="img" aria-label="Herringbone block floor by a white skirting board"></div>
<div class="photo" style="left:489px;top:860px;width:244px;height:232px;background:linear-gradient(180deg,#b7c3b3,#5a605c 45%,#3f4442)" role="img" aria-label="Dark chevron floor beside a glass door"></div>
<div class="photo" style="left:765px;top:860px;width:243px;height:232px;background:linear-gradient(180deg,#a67a4e,#4a4c50 30%,#8e6a45 70%,#a67b50)" role="img" aria-label="Interior with grey cabinets and oak floor"></div>
<div class="service-caption" style="left:211px">Herringbone Blocks</div>
<div class="service-caption" style="left:489px">Chevrons</div>
<div class="service-caption" style="left:765px">Interior Design</div>

<h2 class="section-title" style="top:1185px">Gallery</h2>
<div class="photo" style="left:81px;top:1254px;width:243px;height:184px;background:linear-gradient(180deg,#e6e3de,#d36a2a 55%,#b88c5e)" role="img" aria-label="Orange sofa on light oak floor"></div>
<div class="photo" style="left:81px;top:1460px;width:243px;height:183px;background:linear-gradient(135deg,#e8e3dc,#d8c9b6)" role="img" aria-label="Pale parquet with a table"></div>
<div class="photo" style="left:346px;top:1254px;width:243px;height:389px;background:linear-gradient(180deg,#5a5650,#3c3733 50%,#2c2826)" role="img" aria-label="Bedroom with herringbone blocks">
  <div class="gallery-overlay"><h3>Herringbone<br>Blocks</h3><p>Lorem Ipsum is simply dummy text of the printing and typeset in the industry.</p></div>
</div>
<div class="photo" style="left:611px;top:1254px;width:243px;height:184px;background:linear-gradient(180deg,#e3dfdb,#b9aea3 55%,#8d7a66)" role="img" aria-label="Bed with cushions on wood floor"></div>
<div class="photo" style="left:611px;top:1460px;width:243px;height:183px;background:linear-gradient(135deg,#c7a27c,#a88461 60%,#5f8f9a)" role="img" aria-label="Chair on oak planks"></div>
<div class="photo" style="left:876px;top:1254px;width:243px;height:389px;background:linear-gradient(180deg,#5f6a74,#7c8189 40%,#a58867 75%,#8f7052)" role="img" aria-label="Living room with grey sofa and wide oak planks"></div>
<div class="btn" style="left:541px;top:1679px;width:124px;height:32px">View More</div>

<section class="history">
  <div class="abs" style="left:124px;top:180px;width:410px">
    <h2>History</h2><div class="underline"></div>
    <p class="body" style="margin-bottom:12px">Lorem Ipsum is simply dummy text of the printing and wood typesetting industry.</p>
    <p class="body">Lorem Ipsum has been the industry's standard dummy text a ever since the 1500s, when an unknown printer took a galley of type and scrambled it to make a type specimen book</p>
    <div class="btn" style="position:relative;margin-top:18px;width:124px;height:32px">Read More</div>
  </div>
  <div class="abs" style="left:568px;top:54px" role="img" aria-label="Collage of forest and stacked log photographs">
    <svg width="520" height="482" viewBox="0 0 520 482">
      <rect x="0" y="0" width="122" height="120" fill="#4f6a2e"/>
      <rect x="0" y="126" width="122" height="210" fill="#8c6a42"/>
      <rect x="0" y="342" width="122" height="140" fill="#5d5a34"/>
      <rect x="132" y="80" width="124" height="120" fill="#3f5a2a"/>
      <rect x="132" y="206" width="124" height="192" fill="#b38350"/>
      <rect x="265" y="0" width="122" height="80" fill="#56702f"/>
      <rect x="265" y="86" width="122" height="250" fill="#c09058"/>
      <rect x="265" y="342" width="122" height="140" fill="#6b6338"/>
      <rect x="396" y="80" width="124" height="120" fill="#4a6530"/>
      <rect x="396" y="206" width="124" height="192" fill="#9d7548"/>
    </svg>
  </div>
</section>

<section class="about">
  <div class="photo" style="left:81px;top:2446px;width:365px;height:290px;background:linear-gradient(180deg,#c9ccd0,#8d9196 50%,#6e6a64)" role="img" aria-label="Flooring workshop with machinery and staff"></div>
  <div class="photo" style="left:468px;top:2446px;width:170px;height:135px;background:linear-gradient(135deg,#d9c49c,#b59266)" role="img" aria-label="Hands fitting a wood block"></div>
  <div class="photo" style="left:468px;top:2602px;width:170px;height:134px;background:linear-gradient(135deg,#c8b9a5,#8e7a64)" role="img" aria-label="Stacks of timber in the workshop"></div>
  <div class="abs" style="left:689px;top:2465px;width:420px">
    <div class="eyebrow">About us</div>
    <h2 style="line-height:34px">who we are</h2><div class="underline" style="margin-bottom:16px"></div>
    <p class="body" style="margin-bottom:12px">Lorem Ipsum is simply dummy text of the printing and wood typesetting industry.</p>
    <p class="body">Lorem Ipsum has been the industry's standard dummy text a ever since the 1500s, when an unknown printer took a galley of type and scrambled it to make a type specimen book</p>
    <div class="btn" style="position:relative;margin-top:18px;width:124px;height:32px">Read More</div>
  </div>
</section>

<h2 class="section-title" style="top:2777px">Our Blog</h2>
<article class="blog-card" style="left:81px">
  <div class="photo" style="left:0;top:0;width:327px;height:203px;background:linear-gradient(160deg,#5f7a3a,#2f3f1c 60%,#5a4a2e)" role="img" aria-label="Forest with ferns"></div>
  <div class="blog-meta"><span>Mar 28 , 2019</span><span class="stats"><svg width="12" height="12" viewBox="0 0 12 12" fill="none" stroke="#222"><circle cx="6" cy="6" r="4.5"/></svg>20 <svg width="12" height="12" viewBox="0 0 12 12" fill="none" stroke="#222"><path d="M6 10L2 6a2.2 2.2 0 0 1 4-3 2.2 2.2 0 0 1 4 3z"/></svg>12</span></div><div class="blog-rule"></div>
  <h3>What is Lorem Ipsum?</h3>
  <p>Lorem Ipsum is simply dummy text of the printing and typesetting industry. Lorem Ipsum has been the standard dummy.</p>
  <span class="blog-link">Read More..</span>
</article>
<article class="blog-card" style="left:435px">
  <div class="photo" style="left:0;top:0;width:327px;height:203px;background:linear-gradient(180deg,#e3e0dc,#bfb3a5 50%,#b08a5e)" role="img" aria-label="Kitchen with oak floor"></div>
  <div class="blog-meta"><span>Mar 28 , 2019</span><span class="stats"><svg width="12" height="12" viewBox="0 0 12 12" fill="none" stroke="#222"><circle cx="6" cy="6" r="4.5"/></svg>20 <svg width="12" height="12" viewBox="0 0 12 12" fill="none" stroke="#222"><path d="M6 10L2 6a2.2 2.2 0 0 1 4-3 2.2 2.2 0 0 1 4 3z"/></svg>12</span></div><div class="blog-rule"></div>
  <h3 style="font-weight:400">What is Lorem Ipsum?</h3>
  <p>Lorem Ipsum is simply dummy text of the printing and typesetting industry. Lorem Ipsum has been the standard dummy.</p>
  <span class="blog-link">Read More..</span>
</article>
<article class="blog-card" style="left:792px">
  <div class="photo" style="left:0;top:0;width:327px;height:203px;background:linear-gradient(170deg,#6f7d4a,#a24a26 60%,#7a3a1e)" role="img" aria-label="Autumn forest with red leaves"></div>
  <div class="blog-meta"><span>Mar 28 , 2019</span><span class="stats"><svg width="12" height="12" viewBox="0 0 12 12" fill="none" stroke="#222"><circle cx="6" cy="6" r="4.5"/></svg>20 <svg width="12" height="12" viewBox="0 0 12 12" fill="none" stroke="#222"><path d="M6 10L2 6a2.2 2.2 0 0 1 4-3 2.2 2.2 0 0 1 4 3z"/></svg>12</span></div><div class="blog-rule"></div>
  <h3 style="font-weight:400">What is Lorem Ipsum?</h3>
  <p>Lorem Ipsum is simply dummy text of the printing and typesetting industry. Lorem Ipsum has been the standard dummy.</p>
</article>
<div class="btn" style="left:541px;top:3260px;width:124px;height:32px">Read More</div>

<h2 class="section-title" style="top:3334px">Contact us</h2>
<div class="field" style="left:235px;top:3403px;width:243px;height:44px">Name*</div>
<div class="field" style="left:492px;top:3403px;width:243px;height:44px">Phone*</div>
<div class="field" style="left:749px;top:3403px;width:240px;height:44px">Email*</div>
<div class="field" style="left:235px;top:3460px;width:754px;height:111px">Message</div>
<div class="btn" style="left:541px;top:3587px;width:124px;height:32px">Send</div>

<footer class="site-footer">
  <div class="footer-brand"><div class="brand-mark"></div><div class="brand-name">BELLHAVEN</div></div>
  <div class="footer-col abs" style="left:316px;top:72px">
    <h4>Quick Link</h4><div class="rule"></div>
    <ul><li>Home</li><li>About us</li><li>Services</li><li>Gallery</li><li>History</li><li>Contact us</li></ul>
  </div>
  <div class="footer-col abs" style="left:505px;top:72px">
    <h4>Contact us</h4><div class="rule"></div>
    <div class="contact-list">A : 123th Street,<br>&nbsp;&nbsp;&nbsp;&nbsp;&nbsp;City, UK<br>P : +44 (0)20 7946 0321<br>&nbsp;&nbsp;&nbsp;&nbsp;&nbsp;+44 (0) 7700 900 482<br>E : enquire@bellhaven.co.uk</div>
  </div>
  <div class="footer-col abs" style="left:841px;top:72px">
    <h4>Subscribe to our newsletter</h4><div class="rule"></div>
    <div style="font-size:12px">To receive the latest news &amp; update</div>
    <div class="newsletter-input">Email Here</div>
    <div class="newsletter-btn">Submit</div>
  </div>
  <div class="footer-rule"></div>
  <div class="copyright">Copyright © Bellhaven. All Right Reserved</div>
  <div class="social" style="left:958px;top:313px"><i></i><i></i><i></i><i></i><i></i><i></i></div>
</footer>

</body>
</html>
```